The Maple Sprout Clinic needs a Letterhead

We are a bilingual pediatric clinic located in Montreal, Canada.

Our english name is Maple Sprout Clinic
Our french name is Clinique du petit ruisseau

We offer complete care for children including general pediatric care, pediatric specialist care such as Ear, Nose and Throat, Urology, Neurology and Adolescent Medicine. We also have paramedical specialists such as psychologists, social workers, occupational therapists, speech and language pathologists.

The letterhead must use and be harmonious with our new logo. See Design #4923293. We need two types of letterhead. One for a the Logo and both english and french names on the top and the second with the list of current staff on the left. I have uploaded two old examples for you to see. Thanks and good luck.

Font styles to use
Sans Serif

Colors
3176b5
9d9d9d

Requirements
Must have
• Include our logo.
Nice to have
• Most of our printing is done in black and white. So a grayscale design is fine.
I have included a color and grayscale versions of our logo.

We prefer clean modern designs.

```html
<!DOCTYPE html>
<html lang="en">
<head>
<meta charset="utf-8">
<title>Maple Sprout Clinic – Letterhead</title>
<link rel="stylesheet" href="https://fonts.googleapis.com/css2?family=Saira+Semi+Condensed:wght@400;500&family=Noto+Sans:wght@400;700&display=swap">
<style>
  :root {
    --backdrop: #8d908f;
    --navy: #13202f;
    --paper: #ffffff;
    --periwinkle: #7b86c6;
    --plum: #7a5c96;
    --logo-blue: #5f74b8;
    --ghost: #ecedf4;
  }
  * { margin: 0; padding: 0; box-sizing: border-box; }
  html, body { width: 1200px; height: 900px; overflow: hidden; }
  body { background: var(--backdrop); position: relative; font-family: "Noto Sans", sans-serif; }

  .letterhead {
    position: absolute; left: 305px; top: 14px; width: 592px; height: 872px;
    background: var(--navy);
  }
  .brand {
    position: absolute; left: 28px; top: 24px;
    display: flex; align-items: center; gap: 10px;
    font-family: "Saira Semi Condensed", sans-serif; font-weight: 400;
    font-size: 16px; line-height: 1.1; color: var(--logo-blue);
  }
  .brand-dot { width: 18px; height: 18px; border-radius: 50%; background: var(--logo-blue); flex: none; }

  .masthead {
    position: absolute; right: 34px; top: 14px; text-align: right;
    font-family: "Saira Semi Condensed", sans-serif; font-weight: 500;
  }
  .masthead-en { font-size: 27px; color: var(--periwinkle); line-height: 1.1; }
  .masthead-fr { font-size: 20px; color: var(--plum); line-height: 1.1; }

  .writing-area {
    position: absolute; left: 170px; top: 87px; width: 422px; height: 721px;
    background: var(--paper); border-bottom-left-radius: 14px; overflow: hidden;
  }
  .writing-area .watermark { position: absolute; left: 122px; top: 80px; }

  .staff-list {
    position: absolute; right: 440px; top: 147px; width: 160px; text-align: right;
    color: var(--periwinkle);
  }
  .staff-group { margin-bottom: 12px; }
  .staff-group.wide { margin-bottom: 20px; }
  .staff-group h3 { font-size: 9.2px; font-weight: 700; line-height: 1.15; white-space: nowrap; }
  .staff-group p { font-size: 7.6px; line-height: 1.3; }

  .footer {
    position: absolute; left: 0; right: 0; top: 810px; text-align: center;
    font-family: "Saira Semi Condensed", sans-serif; font-weight: 500;
    font-size: 21px; line-height: 1.25; color: var(--periwinkle);
  }
</style>
</head>
<body>
  <div class="letterhead">
    <div class="brand">
      <span class="brand-dot"></span>
      <span>Maple Sprout Clinic</span>
    </div>

    <header class="masthead">
      <div class="masthead-en">Maple Sprout Clinic</div>
      <div class="masthead-fr">Clinique du petit ruisseau</div>
    </header>

    <aside class="staff-list">
      <section class="staff-group wide">
        <h3>Addresse / Address</h3>
        <p>2285 rue des Érables<br>Suite 210<br>Laval, Qc<br>H7N 2K5<br>Tél. (514) 555-0148<br>Fax. (514) 555-0172</p>
      </section>
      <section class="staff-group wide">
        <h3>Pédiatres / Pediatricians</h3>
        <p>L. Bouchard<br>K. Lindqvist<br>P. Morency<br>E. Tanaka<br>G. Fortier<br>A.Okafor<br>S.Delorme</p>
      </section>
      <section class="staff-group">
        <h3>Neurologue / Neurologist</h3>
        <p>J. Caron</p>
      </section>
      <section class="staff-group">
        <h3>O.R.L. / E.N.T.</h3>
        <p>R. Haddad</p>
      </section>
      <section class="staff-group">
        <h3>Urologue / Urologist</h3>
        <p>V. Novak</p>
      </section>
      <section class="staff-group">
        <h3>Psychologues / Psychologists</h3>
        <p>M. Lefebvre<br>C. Dufresne</p>
      </section>
      <section class="staff-group">
        <h3>Travailleuse social / Social worker</h3>
        <p>N. Pelletier</p>
      </section>
      <section class="staff-group">
        <h3>Dietetiste / Dietician</h3>
        <p>T. Gagnon</p>
      </section>
      <section class="staff-group">
        <h3>Gerante / Manager</h3>
        <p>B.Rinaldi</p>
      </section>
    </aside>

    <main class="writing-area">
      <svg class="watermark" width="490" height="490" viewBox="0 0 490 490" aria-hidden="true">
        <circle cx="245" cy="245" r="245" fill="var(--ghost)"/>
      </svg>
    </main>

    <footer class="footer">
      <div>2285 rue des Érables, Suite 210 Laval, Qc, H7N 2K5</div>
      <div>Tel (514) 555-0148 Fax (514) 555-0172</div>
    </footer>
  </div>
</body>
</html>
```